Stella Marina packaging design

Hi there,
I'm trying to get an outstanding and unique design for my new product.I'm in baby products business.We are launching an organic,100% burp cloth for our online store. The packaging design is very important to our business.We are looking for something simple and unique.Our brand name is Stella Marina which means Sea Star in Italian. We also have dolphin prints on the burp cloth. Our burp cloth made of organic, hypoallergenic, breathable and ultra soft 100% cotton.Each box has 5 burp cloth. Its made with love and care for delicate and sensitive baby skin.I will attach samples of the burp cloth colors for you to get an idea about the product.

baby product

• Our Logo, ORVA image , and made of organic, hypoallergenic, breathable and ultra soft 100% cotton,has 5 burp cloth. Its made with love and care for delicate and sensitive baby skin.I will attach samples of the burp cloth colors for you to get an idea about the product.
• We are looking for something different and can Standout , please to don't make design that has the exact idea of the template that I provide.

```html
<!DOCTYPE html>
<html lang="en">
<head>
<meta charset="utf-8">
<title>Stella Marina – Burp Cloth Box Dieline</title>
<link rel="stylesheet" href="https://fonts.googleapis.com/css2?family=Ubuntu:wght@500;700&family=Open+Sans:wght@400;700&display=swap">
<style>
  :root {
    --bg: #f3fb85;
    --board: #86703b;
    --board-dark: #6a5631;
    --flap-dark: #5f4b2e;
    --panel-box: #6f5b33;
    --lime: #9be22a;
    --lime-soft: #a8e83a;
    --white: #ffffff;
    --window: #f3fb85;
    --window-edge: #a08a4e;
  }
  html, body { margin: 0; padding: 0; overflow: hidden; background: var(--bg); }
  .dieline { display: block; width: 1200px; height: 1200px; }
  .brand { font-family: "Ubuntu", sans-serif; font-weight: 700; fill: var(--lime); }
  .body-text { font-family: "Open Sans", sans-serif; fill: var(--lime); }
  .strong { font-weight: 700; }
  .board { fill: var(--board); }
  .board-dark { fill: var(--board-dark); }
  .flap-dark { fill: var(--flap-dark); }
  .glue-flap { fill: var(--white); }
  .corner-blob { fill: var(--lime); }
  .window { fill: var(--window); stroke: var(--window-edge); stroke-width: 4; }
  .feature-box { fill: var(--panel-box); stroke: #7d6a3c; stroke-width: 2; }
  .cert-band { fill: var(--board-dark); }
  .seal-oval { fill: var(--board-dark); }
  .cert-badge { fill: none; stroke: var(--lime); stroke-width: 2.5; }
  .name-dot { fill: var(--lime); }
  .pack-label { font-family: "Open Sans", sans-serif; fill: var(--board-dark); }
</style>
</head>
<body>
<svg class="dieline" viewBox="0 0 1000 1000" xmlns="http://www.w3.org/2000/svg">

  <!-- glue and tuck flaps -->
  <g class="flaps">
    <path class="glue-flap" d="M66 298 L70 228 L114 228 L118 298 Z"/>
    <path class="glue-flap" d="M66 724 L70 796 L114 796 L118 724 Z"/>
    <path class="glue-flap" d="M498 298 L502 228 L546 228 L550 298 Z"/>
    <path class="glue-flap" d="M498 724 L502 796 L546 796 L550 724 Z"/>
    <rect class="glue-flap" x="555" y="208" width="377" height="32"/>
    <rect class="glue-flap" x="555" y="788" width="377" height="26"/>
    <rect class="glue-flap" x="932" y="298" width="40" height="426"/>
  </g>

  <!-- side panel left -->
  <rect class="board-dark" x="62" y="298" width="58" height="426"/>
  <path class="corner-blob" d="M62 298 H120 V312 Q108 330 96 340 Q80 360 62 372 Z"/>
  <text class="pack-label" font-size="13" transform="translate(84 355) rotate(-90)">5 pack</text>
  <text class="brand" font-size="14" transform="translate(89 700) rotate(-90)">Stella</text>
  <text class="brand" font-size="14" transform="translate(104 700) rotate(-90)">Marina</text>
  <text class="body-text" font-size="13" transform="translate(96 620) rotate(-90)">certified <tspan class="strong">organic cotton</tspan> burp cloth</text>
  <text class="brand" font-size="18" transform="translate(113 515) rotate(-90)">100%</text>

  <!-- back panel -->
  <rect class="board" x="120" y="298" width="377" height="426"/>
  <circle class="name-dot" cx="318" cy="352" r="16"/>
  <text class="brand" font-size="16" x="318" y="398" text-anchor="middle">Stella Marina</text>
  <text class="brand" font-size="16" x="310" y="469" text-anchor="middle">100%</text>
  <text class="body-text" font-size="11.5" x="311" y="487" text-anchor="middle">CERTIFIED <tspan class="strong">ORGANIC COTTON</tspan> BURP CLOTH</text>
  <rect class="feature-box" x="165" y="518" width="290" height="132" rx="8"/>
  <g class="body-text" font-size="12.5">
    <text x="175" y="540">•</text><text x="195" y="540">Ultra-Soft, breathable, Hypoallergenic</text>
    <text x="175" y="558">•</text><text x="195" y="558">Eco-friendly</text>
    <text x="175" y="577">•</text><text x="195" y="577">5 burp cloth per pack</text>
    <text x="175" y="595">•</text><text x="195" y="595">Suitable for baby delicate sensitive skin</text>
    <text x="175" y="614">•</text><text x="195" y="614">Super absorbent</text>
    <text x="175" y="632">•</text><text x="195" y="632">Made with love for little ones</text>
  </g>
  <text class="brand" font-size="13" x="410" y="687" text-anchor="middle">Stella</text>
  <text class="brand" font-size="13" x="410" y="700" text-anchor="middle">Marina</text>

  <!-- side panel right -->
  <rect class="board-dark" x="497" y="298" width="55" height="426"/>
  <path class="corner-blob" d="M552 724 H497 V700 Q510 680 525 672 Q540 662 552 652 Z"/>
  <text class="pack-label" font-size="13" transform="translate(531 672) rotate(90)">5 pack</text>
  <text class="brand" font-size="14" transform="translate(530 326) rotate(90)">Stella</text>
  <text class="brand" font-size="14" transform="translate(515 326) rotate(90)">Marina</text>
  <text class="body-text" font-size="13" transform="translate(522 405) rotate(90)">certified <tspan class="strong">organic cotton</tspan> burp cloth</text>
  <text class="brand" font-size="18" transform="translate(505 497) rotate(90)">100%</text>

  <!-- top tuck flap -->
  <rect class="flap-dark" x="555" y="240" width="377" height="58"/>
  <text class="brand" font-size="20" text-anchor="middle" transform="translate(745 262) rotate(180)">Stella</text>
  <text class="brand" font-size="20" text-anchor="middle" transform="translate(745 284) rotate(180)">Marina</text>

  <!-- front panel -->
  <rect class="board" x="552" y="298" width="380" height="426"/>
  <rect class="board-dark" x="932" y="298" width="28" height="426"/>
  <path class="corner-blob" d="M932 298 H862 Q868 318 888 330 Q905 345 932 352 Z"/>
  <text class="pack-label" font-size="13" x="902" y="323" text-anchor="middle">5 pack</text>
  <text class="brand" font-size="20" x="575" y="337">Stella</text>
  <text class="brand" font-size="20" x="575" y="360">Marina</text>
  <circle class="name-dot" cx="740" cy="332" r="14"/>
  <text class="brand" font-size="8" x="740" y="362" text-anchor="middle">Stella Marina</text>
  <rect class="window" x="617" y="390" width="256" height="158" rx="6"/>
  <ellipse class="seal-oval" cx="745" cy="580" rx="48" ry="56"/>
  <rect class="cert-band" x="555" y="568" width="377" height="20"/>
  <text class="brand" font-size="17" x="745" y="558" text-anchor="middle">100%</text>
  <text class="body-text" font-size="11.5" x="745" y="583" text-anchor="middle">CERTIFIED <tspan class="strong">ORGANIC COTTON</tspan> BURP CLOTH</text>
  <rect class="window" x="617" y="610" width="256" height="62" rx="6"/>
  <circle class="cert-badge" cx="745" cy="695" r="13"/>

  <!-- bottom tuck flap -->
  <rect class="flap-dark" x="555" y="724" width="377" height="64"/>
  <text class="brand" font-size="20" x="743" y="751" text-anchor="middle">Stella</text>
  <text class="brand" font-size="20" x="743" y="774" text-anchor="middle">Marina</text>
</svg>
</body>
</html>
```